Online marketing material for open-source survey & experience management platform
Zielgruppe
Quellwise is an open-source survey & experience management platform that enables organizations to collect feedback securely and with full control over their data.
Our target audience includes two main groups:
1. Developers who rely on and value open-source technologies, and prefer customizable, transparent, and self-hostable tools.
2. Senior decision-makers in larger organizations who need to self-host survey data to meet privacy, security, and compliance requirements.
We help both audiences gather valuable user insights while maintaining full control over their data.
Aufgabenstellung
Define & Apply a New Visual Direction for B2B SaaS
Problem: We already have a 'look & feel' but it's a bit all over the place and we struggle to keep it consistent across all marketing materials. We're looking for find a designer who can help us do that in the medium- to long-term.
Goal: Develop a cohesive visual language for Quellwise’ marketing presence that reflects our identity as an open-source, privacy-first survey platform, and apply it across both Pinvale and web assets. We don't want you to reinvent the wheel or reinvent Quellwise, we would like you to analyze what's there, make it 30% better and help us create assets for our marketing mateirals.
The project is divided into two parts:
1️⃣ Part 1: Define a Visual Direction
- Explore and propose a visual direction that aligns with Quellwise’ identity and values.
- Develop a rough outline of the new or improved Brand Look & Feel (based on examples, iterations, and light brainstorming).
- This doesn’t need to be fully polished, but the direction should be clear and well-justified.
Deliverable: a short visual direction rationale (on a Figma board) explaining:
-Key visual principles
-Chosen colors, typography, and layout approach
-How it appeals to both developers and enterprise decision-makers
2️⃣ Part 2: Apply the Visual Direction
Using the new style, redesign or create visuals to some of the following:
1. Redesign 3 existing Pinvale posts
Use these specific posts as the base you can work with:
https://www.pinvale.example/post/5820193746
https://www.pinvale.example/post/5820193747
https://www.pinvale.example/post/5820193748
3. Redesign some of the graphics of this page
https://quellwise.example/open-source-form-builder
Goal: See your work in action! You don't have..

```html
<!DOCTYPE html>
<html lang="en">
<head>
<meta charset="utf-8">
<title>Quellwise – Visual Direction Applied</title>
<link href="https://fonts.googleapis.com/css2?family=Jost:wght@400;500;600&display=swap" rel="stylesheet">
<style>
  :root{
    --teal:#00c4b8;
    --teal-deep:#0a6f6c;
    --night:#0e1321;
    --night-2:#151b2c;
    --ink:#02041a;
    --navy:#1c2540;
    --frame:#2f5f63;
    --board-top:#fafafa;
    --board-bottom:#e2e2e2;
    --caption:#3a3a3a;
    --white:#f2f4f8;
    --panel-top:#ffffff;
    --panel-bottom:#d9d9dc;
  }
  *{box-sizing:border-box;margin:0;padding:0}
  html,body{width:829px;height:1200px;overflow:hidden}
  body{
    font-family:"Jost",sans-serif;
    background:linear-gradient(180deg,var(--board-top),var(--board-bottom));
    position:relative;
  }
  .post{position:absolute;overflow:hidden;background:var(--night)}
  .caption{position:absolute;font-size:11px;color:var(--caption);letter-spacing:.1px}
  .card{
    position:absolute;border:1.5px solid var(--frame);border-radius:20px;
    background:linear-gradient(155deg,var(--ink) 20%,var(--navy) 100%);
    box-shadow:0 8px 24px rgba(0,0,0,.45);
  }
  .headline{color:var(--teal);font-weight:500;letter-spacing:-2px;line-height:.9}
  .sub{color:var(--white);font-weight:400}
  .pill{
    position:absolute;height:22px;border-radius:11px;border:1px solid #3a4660;
    background:var(--ink);color:var(--white);font-size:7px;letter-spacing:1.3px;
    display:flex;align-items:center;justify-content:center;font-weight:500;
  }
  .glow{position:absolute;border-radius:50%;filter:blur(30px);background:var(--teal-deep)}

  /* post 1 */
  .post-problems{left:66px;top:52px;width:316px;height:395px}
  .post-problems .card{left:19px;top:45px;width:279px;height:267px}
  .post-problems .headline{position:absolute;left:40px;top:96px;font-size:52px}
  .post-problems .sub{position:absolute;left:41px;top:199px;font-size:18px}
  .post-problems .pill{left:163px;top:273px;width:113px}
  .post-problems .cta{position:absolute;left:243px;top:364px;color:var(--white);font-size:14.5px}

  /* post 2 */
  .post-launch{left:410px;top:52px;width:352px;height:352px}
  .post-launch .card{left:19px;top:74px;width:315px;height:181px}
  .post-launch .headline{position:absolute;left:40px;top:96px;font-size:57px;letter-spacing:-2.5px}
  .post-launch .sub{position:absolute;left:41px;top:198px;font-size:18px}
  .post-launch .pill{left:222px;top:242px;width:113px}
  .orb{position:absolute;border-radius:50%;background:radial-gradient(circle at 60% 40%,#0a0f1c,#02040c);border:1px solid #1f3a40;box-shadow:0 6px 18px rgba(0,0,0,.6)}
  .orb-top{left:273px;top:26px;width:88px;height:88px}
  .orb-bottom{left:8px;top:247px;width:124px;height:124px}

  /* post 3 */
  .post-suit{left:410px;top:450px;width:350px;height:183px}
  .post-suit .suit-photo{position:absolute;left:150px;top:0;width:200px;height:183px;
    background:linear-gradient(160deg,#2b2e3a 0%,#1a1d28 45%,#0e1018 80%)}
  .post-suit .card{left:19px;top:65px;width:277px;height:140px}
  .post-suit .lead{position:absolute;left:39px;top:79px;font-size:13.5px;color:var(--white)}
  .post-suit .headline{position:absolute;left:38px;top:100px;font-size:30px;letter-spacing:-1px;line-height:1}
  .post-suit .pill{left:218px;top:146px;width:113px}

  /* web */
  .web{left:212px;top:723px;width:550px;height:309px}
  .web .card{left:26px;top:33px;width:389px;height:253px;border-radius:3px}
  .web .title{position:absolute;left:55px;top:63px;font-size:21px;color:var(--teal);font-weight:400}
  .cat{position:absolute;width:161px;height:58px;border-radius:10px;
    background:linear-gradient(135deg,#d8d8d8,#6c6c6c 60%,#2a2a2a)}
  .cat.selected{border:1px solid var(--teal);box-shadow:0 0 10px rgba(0,196,184,.5)}
  .cat-1{left:55px;top:110px}
  .cat-2{left:228px;top:110px;background:linear-gradient(135deg,#f0f0f0,#a8a8a8)}
  .cat-3{left:55px;top:180px;background:linear-gradient(135deg,#bdbdbd,#7a7a7a)}
  .cat-4{left:228px;top:180px;background:linear-gradient(135deg,#ffffff,#9a9a9a)}
  .check{position:absolute;width:14px;height:14px;border-radius:3px}
  .check.on{left:190px;top:117px;background:var(--teal)}
  .check.off{left:190px;top:187px;background:var(--ink)}
  .btn{position:absolute;top:253px;width:88px;height:17px;border-radius:9px;font-size:5.5px;
    letter-spacing:.8px;display:flex;align-items:center;justify-content:center}
  .btn-back{left:55px;border:1px solid #1f3e4c;color:var(--teal)}
  .btn-next{left:300px;background:var(--teal);color:var(--ink)}
  .setting{position:absolute;left:318px;width:212px;height:49px;border-radius:10px;
    background:linear-gradient(90deg,var(--panel-top),var(--panel-bottom));
    box-shadow:0 4px 12px rgba(0,0,0,.35);display:flex;align-items:center;padding-left:23px;
    font-size:17px;color:#111}
  .setting-brand{top:83px}
  .setting-bg{top:138px}
  .setting-round{top:194px}
  .swatch{position:absolute;left:149px;top:10px;width:52px;height:29px;border-radius:6px;border:1px solid #9aa}
  .swatch.teal{background:var(--teal)}
  .swatch.dark{background:linear-gradient(180deg,var(--navy),var(--ink))}
  .swatch.value{background:#f4f4f4;color:#999;font-size:10px;display:flex;align-items:center;justify-content:center}

  .brand{position:absolute;left:608px;top:1138px;display:flex;align-items:center;gap:12px}
  .brand-mark{width:16px;height:16px;background:var(--teal);border-radius:3px}
  .brand-name{font-size:26px;font-weight:600;color:#0b0f1d;letter-spacing:-.5px}
</style>
</head>
<body>

<section class="post post-problems">
  <div class="glow" style="left:170px;top:300px;width:200px;height:140px"></div>
  <div class="card"></div>
  <h2 class="headline">99<br>Problems</h2>
  <p class="sub">but Compliance ain’t one.</p>
  <div class="pill">HOSTING</div>
  <span class="cta">Hit me ›</span>
</section>
<p class="caption" style="left:66px;top:459px">Social Post, 1080 X 1350px</p>

<section class="post post-launch">
  <div class="glow" style="left:-40px;top:200px;width:160px;height:180px"></div>
  <div class="card"></div>
  <h2 class="headline">Launching<br>surveys</h2>
  <p class="sub">easier then ever!</p>
  <div class="pill">QUELLWISE 4.0</div>
  <div class="orb orb-top"></div>
  <div class="orb orb-bottom"></div>
</section>
<p class="caption" style="left:410px;top:417px">Social Post, 1200 X 1200px</p>

<section class="post post-suit">
  <div class="suit-photo" role="img" aria-label="Monochrome photo of a tailored suit and shirt"></div>
  <div class="glow" style="left:270px;top:110px;width:120px;height:100px"></div>
  <div class="card"></div>
  <p class="lead">Feels like …</p>
  <h2 class="headline">Custom-made suit,<br>shirt &amp; boots.</h2>
  <div class="pill">FEATURES</div>
</section>
<p class="caption" style="left:410px;top:649px">Social Post, 1200 X 627px</p>

<section class="post web">
  <div class="card"></div>
  <h3 class="title">Choose the cutest cats</h3>
  <div class="cat cat-1 selected" role="img" aria-label="Black and white photo of a cat"></div>
  <div class="cat cat-2" role="img" aria-label="Black and white photo of a kitten"></div>
  <div class="cat cat-3" role="img" aria-label="Black and white photo of a cat"></div>
  <div class="cat cat-4" role="img" aria-label="Cartoon kitten illustration"></div>
  <div class="check on">
    <svg width="14" height="14" viewBox="0 0 14 14"><path d="M3.5 7.2l2.3 2.3 4.7-5" fill="none" stroke="#02041a" stroke-width="1.8" stroke-linecap="round" stroke-linejoin="round"/></svg>
  </div>
  <div class="check off"></div>
  <div class="btn btn-back">BACK</div>
  <div class="btn btn-next">NEXT</div>
  <div class="setting setting-brand">Brand Color<span class="swatch teal"></span></div>
  <div class="setting setting-bg">Background<span class="swatch dark"></span></div>
  <div class="setting setting-round">Roundness<span class="swatch value">15px</span></div>
</section>
<p class="caption" style="left:212px;top:1055px">Web, Graphic Redesign</p>

<div class="brand">
  <span class="brand-mark"></span>
  <span class="brand-name">Quellwise</span>
</div>

</body>
</html>
```